"Porch & Pocket" Book Cover 5.5x8.5

Title of the book is "Porch & Pocket"
Subtitle is "Untangling Ledger Myths"
I've used PixelQuarry on multiple occasions you can look on my Brindle page, Mark Teveroff, to see the covers I've used in the other projects I've done.
The target audience are people who have been tricked to think they can't retire because inflation, i.e. cost of living is going up so much they must work to keep up. There is no evidence of this.
And those are the people I want to reach so they can "Porch...and Pocket."
Target Market(s)
Americans aged 55 and over who are thinking about retirement
Industry/Entity Type
Financial
Requirements
Nice to have
- Keep It Simple, Stupid is my mantra. Just make it pop out when people are browsing
Should not have
- No piggy banks. No old people sitting on a beach.

```html
<!DOCTYPE html>
<html lang="en">
<head>
<meta charset="utf-8">
<title>Porch &amp; Pocket — Book Cover</title>
<link rel="stylesheet" href="https://fonts.googleapis.com/css2?family=Montserrat:wght@700;800;900&display=swap">
<style>
  :root {
    --page-bg: #e2e2e2;
    --sky-top: #4fa6d6;
    --sky-mid: #9fd0ea;
    --sky-haze: #cfe6f1;
    --lake: #2f86b5;
    --lake-deep: #1d4f72;
    --reed: #9b7a4f;
    --title-orange: #f26b0f;
    --title-amber: #f4a235;
    --title-yellow: #f2cc00;
    --retire-yellow: #efd600;
    --accent-red: #9c0000;
    --text-light: #f2f2f2;
  }
  html, body {
    margin: 0;
    width: 1200px;
    height: 1200px;
    overflow: hidden;
    background: var(--page-bg);
  }
  .cover {
    position: absolute;
    left: 210px;
    top: 30px;
    width: 780px;
    height: 1140px;
    box-shadow: 0 18px 40px rgba(0,0,0,0.18);
  }
  .cover svg { display: block; }
  .author, .connector, .subtitle, .title-word {
    font-family: "Montserrat", Arial, sans-serif;
  }
  .author { font-weight: 800; font-size: 37px; fill: var(--text-light); letter-spacing: 1px; }
  .title-word { font-weight: 800; }
  .connector { font-weight: 800; font-size: 28px; fill: var(--accent-red); }
  .subtitle { font-weight: 700; font-size: 38px; fill: var(--text-light); letter-spacing: 0.5px; }
</style>
</head>
<body>
<div class="cover">
  <svg width="780" height="1140" viewBox="0 0 780 1140" xmlns="http://www.w3.org/2000/svg">
    <defs>
      <linearGradient id="sceneTones" x1="0" y1="0" x2="0" y2="1">
        <stop offset="0" stop-color="var(--sky-top)"/>
        <stop offset="0.35" stop-color="var(--sky-mid)"/>
        <stop offset="0.58" stop-color="var(--sky-haze)"/>
        <stop offset="0.62" stop-color="var(--lake)"/>
        <stop offset="0.8" stop-color="var(--reed)"/>
        <stop offset="1" stop-color="var(--lake-deep)"/>
      </linearGradient>
      <linearGradient id="titleFire" x1="0" y1="0" x2="1" y2="0">
        <stop offset="0" stop-color="var(--title-orange)"/>
        <stop offset="0.25" stop-color="var(--title-amber)"/>
        <stop offset="0.5" stop-color="var(--title-yellow)"/>
        <stop offset="0.75" stop-color="var(--title-amber)"/>
        <stop offset="1" stop-color="var(--title-orange)"/>
      </linearGradient>
      <filter id="titleShadow" x="-5%" y="-5%" width="110%" height="115%">
        <feDropShadow dx="3" dy="5" stdDeviation="4" flood-color="#000" flood-opacity="0.35"/>
      </filter>
    </defs>

    <rect class="cover-photo" x="0" y="0" width="780" height="1140" fill="url(#sceneTones)"
          role="img" aria-label="Photo of a blue sky with light clouds over a calm lake, a wooden pier leading out to the water between tall golden reeds"/>

    <text class="author" x="390" y="60" text-anchor="middle">MARK TEVEROFF</text>

    <text class="title-word title-top" x="69" y="277" textLength="663" lengthAdjust="spacingAndGlyphs"
          font-size="268" fill="url(#titleFire)" filter="url(#titleShadow)">PORCH</text>

    <line class="rule" x1="69" y1="313" x2="320" y2="313" stroke="var(--accent-red)" stroke-width="1.5"/>
    <text class="connector" x="402" y="323" text-anchor="middle">AND</text>
    <line class="rule" x1="484" y1="313" x2="734" y2="313" stroke="var(--accent-red)" stroke-width="1.5"/>

    <text class="title-word title-bottom" x="69" y="514" textLength="663" lengthAdjust="spacingAndGlyphs"
          font-size="246" fill="var(--retire-yellow)" filter="url(#titleShadow)">POCKET</text>

    <rect class="subtitle-band" x="48" y="545" width="672" height="111" fill="var(--accent-red)"/>
    <text class="subtitle" x="384" y="614" text-anchor="middle" textLength="620" lengthAdjust="spacingAndGlyphs">UNTANGLING LEDGER MYTHS</text>
  </svg>
</div>
</body>
</html>
```